Business Cards Needed For Veterinary Business

Looking for a business card design for a veterinary blood bank. We would like it to be clean and professional on appearance but still warm and inviting. We would like to utilize our logo and similar coloring. We will use our phone number, email, website, employee name, employee title.

We do not want a bunch of animated animal photos but do not need the style to be as clinical as a laboratory or human medical procedure office.

We are looking for some creative ideas to choose from so that we can generate a standout professional business card for our management team to utilize.

Target Market(s)

professionals

Industry/Entity Type

veterinary

Contact Information for Business Card

employee name, employee title, phone number, website URL, email

Font styles to use
Sans Serif

Colors
0054AA
0677BA
7BADD7
CADEEF
E8F1F8
EB3D1F
EC4F4E
F09395
F8D3D4
FCEDEE

Requirements
Nice to have
• creative design
Should not have
• animated photos

```html
<!DOCTYPE html>
<html lang="en">
<head>
<meta charset="utf-8">
<title>Business Card – Front and Back</title>
<link rel="stylesheet" href="https://fonts.googleapis.com/css2?family=Montserrat:wght@600;700&family=Arimo:ital,wght@0,400;1,400&display=swap">
<style>
  :root {
    --stage: #161616;
    --card: #2c2c2e;
    --card-edge: #38383a;
    --brand-red: #eb3d1f;
    --ink-light: #f4f4f4;
    --ink-muted: #d9d9d9;
    --pattern-dark: #262628;
    --pattern-light: #333336;
  }
  * { box-sizing: border-box; margin: 0; padding: 0; }
  html, body {
    width: 1200px; height: 963px; overflow: hidden;
    background: var(--stage);
  }
  .canvas {
    width: 1200px; height: 963px;
    display: flex; flex-direction: column; align-items: center; justify-content: center;
    gap: 56px;
  }
  .card {
    position: relative;
    width: 700px; height: 400px;
    background: var(--card);
    border-radius: 22px;
    box-shadow: 0 0 0 1px var(--card-edge), 0 18px 40px rgba(0,0,0,.55);
    overflow: hidden;
  }

  /* Brand block */
  .brand { position: absolute; display: flex; align-items: center; gap: 14px; }
  .brand-dot {
    width: 34px; height: 34px; border-radius: 50%;
    background: var(--brand-red); flex: none;
  }
  .brand-name {
    font-family: "Montserrat", sans-serif; font-weight: 700;
    color: var(--ink-light); font-size: 30px; line-height: 1; white-space: nowrap;
  }

  .card-front .brand { left: 0; right: 0; top: 110px; justify-content: center; }

  /* Person */
  .person {
    position: absolute; right: 400px; top: 255px; text-align: right;
  }
  .person-name {
    font-family: "Montserrat", sans-serif; font-weight: 600;
    color: var(--brand-red); font-size: 22px; letter-spacing: 1px; text-transform: uppercase;
    white-space: nowrap;
  }
  .person-title {
    font-family: "Arimo", sans-serif; font-style: italic;
    color: var(--ink-light); font-size: 18px; margin-top: 6px;
  }
  .divider {
    position: absolute; left: 318px; top: 250px;
    width: 1px; height: 96px; background: var(--ink-muted);
  }

  /* Contacts */
  .contacts {
    position: absolute; left: 340px; top: 248px; list-style: none;
    font-family: "Arimo", sans-serif; color: var(--ink-light); font-size: 19px;
  }
  .contacts li { display: flex; align-items: center; gap: 12px; height: 33px; white-space: nowrap; }
  .contacts svg { width: 18px; height: 18px; flex: none; }

  /* Back */
  .pattern-fill {
    position: absolute; inset: 0;
    background: linear-gradient(135deg, var(--pattern-light), var(--pattern-dark) 55%, var(--pattern-light));
  }
  .card-back .brand { right: 48px; bottom: 64px; }
  .card-back .brand-name { font-size: 26px; }
  .card-back .brand-dot { width: 28px; height: 28px; }
</style>
</head>
<body>
<main class="canvas">

  <section class="card card-front" aria-label="Business card front">
    <div class="brand">
      <span class="brand-dot"></span>
      <span class="brand-name">Larkfield Pet Blood Service</span>
    </div>

    <div class="person">
      <p class="person-name">Daniel Porter</p>
      <p class="person-title">Manager</p>
    </div>
    <span class="divider"></span>

    <ul class="contacts">
      <li>
        <svg viewBox="0 0 24 24" aria-hidden="true"><path fill="var(--brand-red)" d="M6.6 10.8a15 15 0 0 0 6.6 6.6l2.2-2.2a1 1 0 0 1 1-.25 11.4 11.4 0 0 0 3.6.57 1 1 0 0 1 1 1V20a1 1 0 0 1-1 1A17 17 0 0 1 3 4a1 1 0 0 1 1-1h3.5a1 1 0 0 1 1 1c0 1.25.2 2.45.57 3.57a1 1 0 0 1-.25 1z"/></svg>
        555-014-2380
      </li>
      <li>
        <svg viewBox="0 0 24 24" aria-hidden="true"><rect x="2.5" y="5" width="19" height="14" rx="1.5" fill="none" stroke="var(--brand-red)" stroke-width="2"/><path d="M3 6l9 7 9-7" fill="none" stroke="var(--brand-red)" stroke-width="2"/></svg>
        daniel@larkfieldpbs.com
      </li>
      <li>
        <svg viewBox="0 0 24 24" aria-hidden="true"><g fill="none" stroke="var(--brand-red)" stroke-width="1.8"><circle cx="12" cy="12" r="9.5"/><ellipse cx="12" cy="12" rx="4.2" ry="9.5"/><path d="M2.5 12h19M4 7h16M4 17h16"/></g></svg>
        www.larkfieldpbs.com
      </li>
    </ul>
  </section>

  <section class="card card-back" aria-label="Business card back">
    <div class="pattern-fill" role="img" aria-label="Repeating tone-on-tone pattern of the brand symbol"></div>
    <div class="brand">
      <span class="brand-dot"></span>
      <span class="brand-name">Larkfield Pet Blood Service</span>
    </div>
  </section>

</main>
</body>
</html>
```